Cups in Quiet Bloom webdesign + shopvantix implementation

Hi there!
We are a brand new small company located in central Europe, specializing in handmade coffee and tea mugs - please check www.cupsinquietbloom.example

We are looking for a complete redesign, something easy, nothing complicated.

1. web desing (smooth and easy - homepage,product detail page, etc...)
2. html/css
3. shopvantix platform implementation

Industry/Entity Type

It Company

```html
<!DOCTYPE html>
<html lang="en">
<head>
<meta charset="utf-8">
<title>Cups in Quiet Bloom</title>
<link href="https://fonts.googleapis.com/css2?family=Open+Sans:wght@300;400;600;700&display=swap" rel="stylesheet">
<style>
:root{
  --page:#f3efdd;
  --band:#e9e2c6;
  --white:#ffffff;
  --brown:#a8762a;
  --brown-dark:#8a5f20;
  --gold:#b98a3b;
  --grey:#7a7468;
  --grey-light:#b7b2a4;
  --frame:#e6e2d4;
  --rule:#dedace;
  --price:#e2405b;
  --soft:#faf8f1;
}
*{margin:0;padding:0;box-sizing:border-box}
html,body{width:1200px;height:2239px;overflow:hidden}
body{position:relative;background:var(--page);font-family:"Open Sans",Arial,sans-serif;color:var(--grey)}
a{color:inherit;text-decoration:none}

.top-links{position:absolute;top:8px;right:119px;font-size:12px;color:var(--brown);display:flex;gap:10px;align-items:center}
.top-links .sep{color:var(--grey-light)}
.top-links svg{width:16px;height:16px;vertical-align:-3px;margin-right:4px}

.header{position:absolute;left:119px;top:40px;width:962px;height:121px;background:var(--white)}
.brand{position:absolute;left:26px;top:30px;display:flex;align-items:center;gap:12px}
.brand-mark{width:22px;height:22px;background:var(--brown);border-radius:50%}
.brand-name{font-size:25px;font-weight:600;color:var(--brown-dark)}
.header-links{position:absolute;right:10px;top:12px;font-size:12px;color:var(--brown)}
.header-links .sep{color:var(--grey-light);margin:0 8px}
.currency{position:absolute;right:10px;top:36px;width:152px;height:32px;border:1px solid var(--rule);display:flex;font-size:12px;font-weight:700;color:var(--grey)}
.currency span{flex:1;padding:7px 8px}
.currency b{width:42px;background:var(--brown)}
.search{position:absolute;right:10px;top:76px;width:210px;height:32px;border:1px solid var(--rule);display:flex;font-size:12px;font-weight:700;color:#555}
.search span{flex:1;padding:7px 8px}
.search b{width:42px;background:var(--brown);display:flex;align-items:center;justify-content:center}

.nav{position:absolute;left:119px;top:161px;width:962px;height:54px;background:var(--band);display:flex;align-items:center;padding-left:14px;box-shadow:0 6px 8px -6px rgba(0,0,0,.2)}
.nav a{font-size:12.5px;color:var(--brown);margin-right:28px;letter-spacing:.3px}
.cart{position:absolute;right:20px;top:17px;font-size:12px;font-weight:600;color:var(--brown);display:flex;align-items:center;gap:6px}

.hero-intro{position:absolute;left:133px;top:238px;width:316px;text-align:center}
.hero-intro p{font-size:12px;letter-spacing:1.4px;line-height:37px;text-transform:uppercase;color:var(--grey);font-weight:600}
.hero-intro .motto{font-size:15px;letter-spacing:0;text-transform:none;color:#5e574b;line-height:26px;margin-top:2px}
.hero-brand{display:flex;align-items:center;justify-content:center;gap:10px;margin-top:26px}
.hero-brand .brand-name{font-size:22px}
.hero-photo{position:absolute;left:497px;top:242px;width:558px;height:291px;background:linear-gradient(180deg,#ece8e2 0%,#d8cfc4 45%,#b26a4e 62%,#a98a66 100%)}
.dots{position:absolute;left:749px;top:540px;display:flex;gap:4px}
.dots i{width:12px;height:12px;border-radius:50%;background:#b58c4a;border:2px solid #e5d8b8}

.content{position:absolute;left:0;top:571px;width:1200px;height:1305px;background:var(--soft)}
.section-title{position:absolute;left:117px;top:22px;font-size:26px;font-weight:400;color:var(--gold)}
.rule{position:absolute;left:119px;width:962px;height:9px;background:var(--rule)}
.row{position:absolute;left:119px;width:962px;display:flex;gap:31px}
.card{width:217px;height:312px;background:var(--frame);padding:8px;box-shadow:0 4px 6px -3px rgba(0,0,0,.15)}
.card-inner{width:100%;height:100%;background:var(--white);padding:18px 13px 0;position:relative}
.card.is-active .card-inner{background:#f1ece0}
.card-photo{height:119px;width:175px;margin:0 auto}
.card-divider{height:1px;background:var(--rule);margin:16px 20px 0}
.card-title{margin-top:24px;font-size:12px;font-weight:700;line-height:15px;color:var(--gold)}
.card-buy{display:flex;justify-content:space-between;align-items:center;margin-top:17px}
.price{font-size:19px;font-weight:700;color:var(--price)}
.view{width:67px;height:29px;background:var(--brown);color:var(--white);font-size:17px;font-weight:700;text-align:center;line-height:28px}
.add-cart{display:flex;align-items:center;justify-content:center;gap:6px;width:124px;height:27px;margin:9px auto 0;border:1px solid #cfcbc0;border-radius:3px;background:linear-gradient(#fbfbf9,#e2e0da);font-size:10px;font-weight:700;color:#666}

.footer{position:absolute;left:0;top:1876px;width:1200px;height:289px;background:var(--page)}
.foot-col{position:absolute;top:56px}
.foot-col h3{font-size:13px;font-weight:700;color:var(--brown);margin-bottom:12px}
.foot-col li{list-style:none;font-size:12px;line-height:26px;color:var(--grey)}
.foot-col li::before{content:"> ";}
.contact li{list-style:none;display:flex;gap:14px;font-size:11.5px;line-height:23px;color:var(--grey);margin-bottom:8px}
.contact li::before{content:none}
.contact svg{flex:none;width:16px;height:16px;margin-top:4px}
.contact .strong{color:var(--brown);font-weight:700}
.map{width:212px;height:172px;background:linear-gradient(160deg,#dde7ef,#a9c0d3 60%,#c9d4c2)}
.bottom{position:absolute;left:0;top:2165px;width:1200px;height:74px;background:var(--band)}
.pay{position:absolute;left:119px;top:26px;display:flex;gap:7px}
.pay i{width:48px;height:28px;border:1px solid #c8c2ad;border-radius:3px;background:var(--white)}
.powered{position:absolute;right:119px;top:30px;font-size:11px;color:var(--grey)}
</style>
</head>
<body>

<div class="top-links">
  <span>Welcome</span><span class="sep">|</span>
  <span><svg viewBox="0 0 16 16"><circle cx="8" cy="5" r="3.5" fill="#8a6a3a"/><path d="M1 16c0-5 3-7 7-7s7 2 7 7z" fill="#8a6a3a"/></svg>Log in</span>
</div>

<header class="header">
  <div class="brand"><span class="brand-mark"></span><span class="brand-name">Cups in Quiet Bloom</span></div>
  <div class="header-links">Contact<span class="sep">|</span>Sitemap</div>
  <div class="currency"><span>Currency:$</span><b></b></div>
  <div class="search"><span>Type Keywords here...</span><b><svg width="16" height="16" viewBox="0 0 16 16"><circle cx="6.5" cy="6.5" r="4.5" fill="none" stroke="#fff" stroke-width="2"/><path d="M10 10l4.5 4.5" stroke="#fff" stroke-width="2.4"/></svg></b></div>
</header>

<nav class="nav">
  <a>HOME PAGE</a><a>CATEGORIES</a><a>NEW ARRIVALS</a><a>ABOUT OUR MUGS</a><a>MY ACCOUNT</a><a>CONTACT US</a>
  <div class="cart"><svg width="26" height="20" viewBox="0 0 26 20"><path d="M2 6h22l-3 12H5z" fill="none" stroke="#a8762a" stroke-width="2"/><path d="M8 6l4-5M18 6l-4-5" stroke="#a8762a" stroke-width="1.6"/></svg>Cart:(empty)</div>
</nav>

<section class="hero-intro">
  <p>Hey coffee lovers! Looking for a unique coffee mug? We offer beautiful handmade coffee mugs and tea cups born in the heart of Europe. Beautiful design, precise execution and piece of a heart.</p>
  <p class="motto">Relax and "Mug the moment"!</p>
  <div class="hero-brand"><span class="brand-mark"></span><span class="brand-name">Cups in Quiet Bloom</span></div>
</section>
<div class="hero-photo" role="img" aria-label="Three hand-painted terracotta cups with flower motifs on a woven mat"></div>
<div class="dots"><i></i><i></i><i></i></div>

<main class="content">
  <h2 class="section-title">Featured products</h2>
  <div class="rule" style="top:59px"></div>

  <div class="row" style="top:89px">
    <div class="card"><div class="card-inner"><div class="card-photo" role="img" aria-label="Red mug with white painted pattern" style="background:linear-gradient(#eee,#c9a7a0 50%,#b5402f)"></div><div class="card-divider"></div><p class="card-title">Lorem ipsum dolor sit amet, consectetur...</p><div class="card-buy"><span class="price">$1500</span><span class="view">view</span></div><div class="add-cart">ADD TO CART</div></div></div>
    <div class="card"><div class="card-inner"><div class="card-photo" role="img" aria-label="White mug with blue painted decoration on a woven mat" style="background:linear-gradient(#7d7a74,#9aa3b5 50%,#b49a78)"></div><div class="card-divider"></div><p class="card-title">Lorem ipsum dolor sit amet, consectetur...</p><div class="card-buy"><span class="price">$1500</span><span class="view">view</span></div><div class="add-cart">ADD TO CART</div></div></div>
    <div class="card"><div class="card-inner"><div class="card-photo" role="img" aria-label="Cream mug with red dots on a woven mat" style="background:linear-gradient(#7a7670,#d7c4ad 50%,#b29672)"></div><div class="card-divider"></div><p class="card-title">Lorem ipsum dolor sit amet, consectetur...</p><div class="card-buy"><span class="price">$1500</span><span class="view">view</span></div><div class="add-cart">ADD TO CART</div></div></div>
    <div class="card"><div class="card-inner"><div class="card-photo" role="img" aria-label="Terracotta mug with painted hearts on a woven mat" style="background:linear-gradient(#7a7670,#c25a48 50%,#b29672)"></div><div class="card-divider"></div><p class="card-title">Lorem ipsum dolor sit amet, consectetur...</p><div class="card-buy"><span class="price">$1500</span><span class="view">view</span></div><div class="add-cart">ADD TO CART</div></div></div>
  </div>

  <div class="rule" style="top:466px"></div>
  <div class="row" style="top:508px">
    <div class="card"><div class="card-inner"><div class="card-photo" role="img" aria-label="Terracotta mug with painted flowers on a woven mat" style="background:linear-gradient(#7a7670,#c35c45 50%,#b29672)"></div><div class="card-divider"></div><p class="card-title">Lorem ipsum dolor sit amet, consectetur...</p><div class="card-buy"><span class="price">$1500</span><span class="view">view</span></div><div class="add-cart">ADD TO CART</div></div></div>
    <div class="card"><div class="card-inner"><div class="card-photo" role="img" aria-label="White mug with blue motif on a woven mat" style="background:linear-gradient(#7a7670,#a3adc0 50%,#b29672)"></div><div class="card-divider"></div><p class="card-title">Lorem ipsum dolor sit amet, consectetur...</p><div class="card-buy"><span class="price">$1500</span><span class="view">view</span></div><div class="add-cart">ADD TO CART</div></div></div>
    <div class="card is-active"><div class="card-inner"><div class="card-photo" role="img" aria-label="Terracotta mug with painted leaves on a woven mat" style="background:linear-gradient(#7a7670,#c46049 50%,#b29672)"></div><div class="card-divider"></div><p class="card-title">Lorem ipsum dolor sit amet, consectetur...</p><div class="card-buy"><span class="price">$1500</span><span class="view">view</span></div><div class="add-cart">ADD TO CART</div></div></div>
    <div class="card"><div class="card-inner"><div class="card-photo" role="img" aria-label="Terracotta mug with white floral pattern on a woven mat" style="background:linear-gradient(#7a7670,#b8503f 50%,#b29672)"></div><div class="card-divider"></div><p class="card-title">Lorem ipsum dolor sit amet, consectetur...</p><div class="card-buy"><span class="price">$1500</span><span class="view">view</span></div><div class="add-cart">ADD TO CART</div></div></div>
  </div>

  <div class="rule" style="top:885px"></div>
  <div class="row" style="top:927px">
    <div class="card"><div class="card-inner"><div class="card-photo" role="img" aria-label="White mug with blue painted pattern on a woven mat" style="background:linear-gradient(#7a7670,#9fa9ba 50%,#b29672)"></div><div class="card-divider"></div><p class="card-title">Lorem ipsum dolor sit amet, consectetur...</p><div class="card-buy"><span class="price">$1500</span><span class="view">view</span></div><div class="add-cart">ADD TO CART</div></div></div>
    <div class="card"><div class="card-inner"><div class="card-photo" role="img" aria-label="Terracotta bowl with white flowers on a woven mat" style="background:linear-gradient(#7a7670,#c0573f 50%,#b29672)"></div><div class="card-divider"></div><p class="card-title">Lorem ipsum dolor sit amet, consectetur...</p><div class="card-buy"><span class="price">$1500</span><span class="view">view</span></div><div class="add-cart">ADD TO CART</div></div></div>
    <div class="card"><div class="card-inner"><div class="card-photo" role="img" aria-label="Terracotta mug with red and yellow flower on a woven mat" style="background:linear-gradient(#7a7670,#c66a4c 50%,#b29672)"></div><div class="card-divider"></div><p class="card-title">Lorem ipsum dolor sit amet, consectetur...</p><div class="card-buy"><span class="price">$1500</span><span class="view">view</span></div><div class="add-cart">ADD TO CART</div></div></div>
    <div class="card"><div class="card-inner"><div class="card-photo" role="img" aria-label="Cream mug with small painted motif on a woven mat" style="background:linear-gradient(#7a7670,#d8ccb8 50%,#b29672)"></div><div class="card-divider"></div><p class="card-title">Lorem ipsum dolor sit amet, consectetur...</p><div class="card-buy"><span class="price">$1500</span><span class="view">view</span></div><div class="add-cart">ADD TO CART</div></div></div>
  </div>
</main>

<footer class="footer">
  <div class="foot-col" style="left:119px"><h3>Company name</h3><ul><li>Home Page</li><li>Categories</li><li>New Arrivals</li><li>About our mugs</li><li>My Account</li></ul></div>
  <div class="foot-col" style="left:358px"><h3>INFORMATION</h3><ul><li>About Store</li><li>Contact Us</li><li>Customer Assistance</li><li>Privacy Policy</li><li>Terms &amp; Condition</li><li>Worldwide Delivery</li></ul></div>
  <div class="foot-col contact" style="left:566px"><h3 style="margin-left:27px">CONTACT US</h3><ul>
    <li><svg viewBox="0 0 16 16"><path d="M8 1a5 5 0 0 0-5 5c0 4 5 9 5 9s5-5 5-9a5 5 0 0 0-5-5z" fill="#444"/><circle cx="8" cy="6" r="2" fill="#fff"/></svg><span>No 12 Linden Row 48/3, Brookvale,<br>BV 20417</span></li>
    <li><svg viewBox="0 0 16 16"><rect x="1" y="3" width="14" height="10" fill="#444"/><path d="M1 3l7 6 7-6" fill="none" stroke="#fff" stroke-width="1.3"/></svg><span class="strong">hello@cupsinquietbloom.example<br>hello@cupsinquietbloom.example</span></li>
    <li><svg viewBox="0 0 16 16"><path d="M3 2h3l1 3-2 1.5a9 9 0 0 0 4.5 4.5L11 9l3 1v3a2 2 0 0 1-2 2C6 15 1 10 1 4a2 2 0 0 1 2-2z" fill="#444"/></svg><span class="strong">(+00) 555 0142-318<br>(+00) 555 0142-318</span></li>
  </ul></div>
  <div class="foot-col" style="left:871px"><h3>AREA MAP</h3><div class="map" role="img" aria-label="World map showing the shop location"></div></div>
</footer>

<div class="bottom">
  <div class="pay"><i></i><i></i><i></i><i></i></div>
  <div class="powered">Powered By: shopvantix 6.0.60</div>
</div>

</body>
</html>
```